Environmentally friendly Café Lune Verte serves fully certified coffee

Hi, I'm looking to improve on my work in process pagerookery website.

Café Lune Verte is a play on words, meaning tomorrow's coffee, between two 'responsible' hands (deux main).

What makes my coffee shop unique is that we will be serving eco responsible fully certified coffee. Our partnership with producers is based on a deep desire to do things differently, responsibly and for farmers and worker communities to be remunerated fairly.

The socioeconomic impact of my coffee shop means that we get the coffee directly and through True Ledger, an organic product with a direct reinvestment to specific farmers and their families.

Clients will play a crucial role in our mission. We will enable our local community to not settle for purchasing coffee, but to become a part of a life-changing story. Our customers will enjoy an unrivaled coffee experience while knowing that each sip connects them to a healthier future and environment.

The 4 certifications are:

True Ledger
Which is about supporting the development of thriving farmers and worker communities that have more control over their futures and protecting the
environment in which they live and work.

Organic
Which refers to the way agricultural products are grown and processed; using environmentally and animal friendly farming methods

Leaf Harbour
Using Hollinwaite conservation science, the Leaf Harbour gold standard does more than other eco-friendly seals to protect quality habitat,
which is often destroyed to make way for coffee growing

Café Solvera
A gender-focused program to support social justice and empowerment for women coffee producers worldwide.

Café Lune Verte has the unique opportunity to get its message, services and products known, admired, and sought out. It is a vital message; that together, with sustainable products, we will help the farmers, who are using exemplary measures to promote the conservation of tropical rainforests as well as to the future of our planet.

Please note my concept (café) introduces the 'brewlane coffee 'machine'

https://red-plum-k7x9.pagerookery.example/config/settings/site-visibility

Password: Castelmoor

Target Market(s)

Professionals, couples, women. Anyone who loves coffee and wants to make an environmental impact .

Industry/Entity Type

café, specialized coffee shop

Requirements
Must have
• Brewlane concept

```html
<!DOCTYPE html>
<html lang="en">
<head>
<meta charset="utf-8">
<title>Café Lune Verte — coffee with a conscious</title>
<link rel="stylesheet" href="https://fonts.googleapis.com/css2?family=Barlow:wght@400;500;600&family=Mrs+Saint+Delafield&display=swap">
<style>
  :root {
    --page: #f9f8f8;
    --ink: #2b2b2b;
    --text: #3a3a3a;
    --pink: #f4b9bc;
    --green: #c9e2b8;
    --blue: #8fa8d8;
    --band: #f6f1f2;
    --footer: #2b2b2b;
    --white: #ffffff;
    --sans: "Barlow", Arial, sans-serif;
    --script: "Mrs Saint Delafield", cursive;
  }
  * { margin: 0; padding: 0; box-sizing: border-box; }
  html, body { width: 1200px; height: 2807px; overflow: hidden; }
  body { position: relative; background: var(--page); font-family: var(--sans); color: var(--text); }
  .abs { position: absolute; }

  /* header */
  .site-header { left: 0; top: 0; width: 1200px; height: 95px; background: var(--page); }
  .brand { left: 113px; top: 30px; font-size: 30px; font-weight: 500; color: var(--ink); letter-spacing: .5px; }
  .nav { left: 624px; top: 36px; display: flex; gap: 20px; font-size: 17px; color: var(--ink); }
  .flag { left: 901px; top: 41px; width: 26px; height: 15px; background: linear-gradient(180deg, #c84a4a 0 50%, #f2f2f2 50% 60%, #c84a4a 60% 100%); }
  .flag::before { content: ""; position: absolute; left: 0; top: 0; width: 11px; height: 8px; background: #3b4f8f; }
  .btn { display: flex; align-items: center; justify-content: center; background: var(--ink); color: var(--white); font-size: 13px; font-weight: 500; border-radius: 3px; text-transform: uppercase; letter-spacing: .2px; }
  .btn-order { left: 966px; top: 27px; width: 123px; height: 42px; }

  /* hero */
  .hero { left: 0; top: 95px; width: 1200px; height: 600px;
    background:
      linear-gradient(180deg, rgba(0,0,0,0) 55%, rgba(10,14,8,.75) 100%),
      radial-gradient(circle at 52% 18%, #d2463a 0%, #a82d24 8%, transparent 16%),
      radial-gradient(circle at 62% 34%, #c43a30 0%, #8e2620 9%, transparent 18%),
      radial-gradient(circle at 46% 40%, #b8352b 0%, #7a2019 8%, transparent 16%),
      radial-gradient(circle at 56% 56%, #a52e27 0%, transparent 12%),
      radial-gradient(circle at 75% 12%, #6aa241 0%, transparent 10%),
      radial-gradient(circle at 8% 28%, #5f9a3a 0%, transparent 10%),
      radial-gradient(ellipse at 90% 45%, #9fc46a 0%, #5f8b35 18%, transparent 40%),
      radial-gradient(ellipse at 15% 60%, #2c4a1c 0%, transparent 45%),
      linear-gradient(110deg, #24391a 0%, #3f6428 35%, #4e7a30 60%, #7fa556 85%, #3a5a24 100%); }
  .hero-title { left: 0; top: 440px; width: 1200px; text-align: center; font-size: 64px; font-weight: 500; color: var(--white); }
  .hero-tag { left: 0; top: 540px; width: 1200px; text-align: center; font-family: var(--script); font-size: 68px; color: var(--white); }

  /* section headings */
  .script-heading { font-family: var(--script); font-weight: 400; font-size: 72px; color: var(--ink); line-height: 1; }
  .rule { display: flex; gap: 4px; }
  .rule span { width: 40px; height: 3px; }
  .rule .p { background: var(--pink); } .rule .g { background: var(--green); } .rule .b { background: var(--blue); }

  /* about */
  .about-heading { left: 0; top: 770px; width: 1200px; text-align: center; }
  .about-rule { left: 537px; top: 855px; }
  .about-copy { left: 230px; top: 893px; width: 740px; text-align: center; font-size: 16px; line-height: 30px; }
  .btn-about { left: 538px; top: 1002px; width: 124px; height: 41px; }

  .menu-card { top: 1098px; width: 226px; height: 313px; border-radius: 2px; overflow: hidden; }
  .menu-card::after { content: ""; position: absolute; left: 0; right: 0; bottom: 0; height: 110px; background: linear-gradient(180deg, rgba(244,185,188,0) 0%, rgba(244,185,188,.8) 100%); }
  .menu-card .label { position: absolute; left: 0; right: 0; bottom: 36px; text-align: center; font-size: 23px; font-weight: 500; color: var(--white); z-index: 1; }
  .card-coffee { left: 113px; background:
      radial-gradient(ellipse 42% 20% at 48% 45%, #e8c08e 0%, #b97842 55%, transparent 100%),
      radial-gradient(ellipse 58% 30% at 48% 48%, #1d1a1a 0%, #141416 70%, transparent 100%),
      radial-gradient(ellipse 40% 25% at 60% 75%, #c58d6c 0%, transparent 100%),
      linear-gradient(170deg, #0e1d38 0%, #17284a 45%, #2b3553 100%); }
  .card-sandwich { left: 363px; background:
      radial-gradient(ellipse 45% 30% at 55% 55%, #8e3a3c 0%, #b4665a 40%, transparent 75%),
      radial-gradient(ellipse 55% 18% at 50% 38%, #e0b872 0%, transparent 100%),
      radial-gradient(ellipse 30% 25% at 15% 20%, #d8c8a8 0%, transparent 100%),
      linear-gradient(170deg, #5e4330 0%, #8a6544 40%, #7a5034 75%, #4c3222 100%); }
  .card-soup { left: 613px; background:
      radial-gradient(ellipse 36% 20% at 52% 42%, #f3a629 0%, #e48a1c 70%, transparent 100%),
      radial-gradient(ellipse 50% 40% at 50% 52%, #f4f0ea 0%, #dcd6cc 70%, transparent 100%),
      linear-gradient(160deg, #6b4428 0%, #8a5c38 40%, #70482c 75%, #4e3220 100%); }
  .card-dessert { left: 863px; background:
      radial-gradient(ellipse 22% 12% at 45% 38%, #c02a44 0%, transparent 100%),
      radial-gradient(ellipse 30% 30% at 45% 58%, #f7f4f0 0%, #e4ddd6 60%, transparent 100%),
      radial-gradient(circle at 92% 85%, #c0283c 0%, transparent 8%),
      radial-gradient(circle at 88% 30%, #c43046 0%, transparent 6%),
      linear-gradient(175deg, #e9e6e3 0%, #d9d4d0 50%, #c8bfb7 100%); }

  /* brewlane */
  .brew-band { left: 0; top: 1510px; width: 1200px; height: 545px; background: var(--band); }
  .brew-heading { left: 110px; top: 1590px; }
  .brew-rule { left: 110px; top: 1672px; }
  .brew-lead { left: 113px; top: 1720px; font-size: 16px; font-weight: 500; color: var(--ink); }
  .brew-copy { left: 113px; top: 1758px; width: 535px; font-size: 16px; line-height: 30px; }
  .btn-brew { left: 113px; top: 1925px; width: 124px; height: 41px; }
  .block-green { left: 720px; top: 1845px; width: 193px; height: 171px; background: var(--green); opacity: .8; }
  .block-pink { left: 1089px; top: 1596px; width: 34px; height: 36px; background: var(--pink); }
  .block-blue { left: 1107px; top: 1640px; width: 41px; height: 37px; background: var(--blue); }
  .brew-photo { left: 751px; top: 1576px; width: 337px; height: 415px; box-shadow: 0 4px 10px rgba(0,0,0,.15);
    background:
      radial-gradient(ellipse 18% 10% at 52% 85%, #48b8a6 0%, #2f9686 70%, transparent 100%),
      radial-gradient(ellipse 30% 10% at 75% 70%, #6a4a32 0%, transparent 100%),
      radial-gradient(ellipse 28% 40% at 40% 40%, #f2f2f0 0%, #b9bab8 45%, transparent 80%),
      linear-gradient(180deg, transparent 85%, #3a3b3c 100%),
      linear-gradient(100deg, #9a9995 0%, #c8c7c3 35%, #a8a7a2 70%, #d9d8d4 100%); }

  /* impact */
  .impact-heading { left: 0; top: 2122px; width: 1200px; text-align: center; }
  .impact-rule { left: 537px; top: 2198px; }
  .cert { top: 2275px; width: 180px; text-align: center; }
  .cert .disc { width: 120px; height: 120px; margin: 0 auto; border-radius: 50%; background: var(--white); box-shadow: 0 3px 8px rgba(0,0,0,.12); display: flex; align-items: center; justify-content: center; }
  .cert .face { width: 106px; height: 106px; border-radius: 50%; display: flex; align-items: center; justify-content: center; }
  .cert svg { width: 52px; height: 52px; fill: none; stroke: var(--white); stroke-width: 2.4; stroke-linecap: round; stroke-linejoin: round; }
  .cert .name { margin-top: 36px; font-size: 21px; color: var(--text); }

  /* footer */
  .site-footer { left: 0; top: 2557px; width: 1200px; height: 250px; background: var(--footer); color: var(--white); }
  .footer-brand { left: 120px; top: 2655px; font-size: 32px; font-weight: 500; color: var(--white); }
  .footer-col { top: 2620px; font-size: 16px; line-height: 30px; color: var(--white); }
  .footer-col svg { display: block; margin-bottom: 4px; }
  .footer-rule { left: 113px; top: 2747px; width: 976px; height: 1px; background: #444; }
  .copyright { left: 0; top: 2768px; width: 1200px; text-align: center; font-size: 16px; color: var(--white); }
</style>
</head>
<body>

<header class="site-header abs">
  <div class="brand abs">Café Lune Verte</div>
  <nav class="nav abs"><span>Home</span><span>Menu</span><span>About</span><span>Contact</span></nav>
  <div class="flag abs" role="img" aria-label="Language flag"></div>
  <div class="btn btn-order abs">Order Now</div>
</header>

<section class="hero abs" role="img" aria-label="Photo of ripe red coffee cherries on a branch among green leaves"></section>
<div class="hero-title abs">Café Lune Verte</div>
<div class="hero-tag abs">__coffee with a conscious__</div>

<h2 class="about-heading script-heading abs">About Us</h2>
<div class="about-rule rule abs"><span class="p"></span><span class="g"></span><span class="b"></span></div>
<p class="about-copy abs">Welcome to the first coffee shop in Castelmoor committed to offering unique, certified organic coffee. It is here at Café Lune Verte that we are giving our community the unique opportunity to make an impact on our environment.</p>
<div class="btn btn-about abs">Learn More</div>

<div class="menu-card card-coffee abs" role="img" aria-label="Photo of a latte with milk art"><span class="label">Café/Beverages</span></div>
<div class="menu-card card-sandwich abs" role="img" aria-label="Photo of a stacked sandwich"><span class="label">Sandwiches</span></div>
<div class="menu-card card-soup abs" role="img" aria-label="Photo of a bowl of squash soup"><span class="label">Soups/Salads</span></div>
<div class="menu-card card-dessert abs" role="img" aria-label="Photo of a yogurt parfait with raspberries"><span class="label">Desserts</span></div>

<section class="brew-band abs"></section>
<h2 class="brew-heading script-heading abs">Brewlane Experience</h2>
<div class="brew-rule rule abs"><span class="p"></span><span class="g"></span><span class="b"></span></div>
<p class="brew-lead abs">Café Lune Verte introduces&nbsp; the beautifully crafted&nbsp; Brewlane experience</p>
<p class="brew-copy abs">Brewlane is a unique revolutionary coffee brewing experience that gives us the freedom to focus on our customers. From the moment the order is placed, to when the coffee is served, our staff will engage interested customers with our coffee bean origins.</p>
<div class="btn btn-brew abs">Learn More</div>
<div class="block-green abs"></div>
<div class="block-pink abs"></div>
<div class="block-blue abs"></div>
<div class="brew-photo abs" role="img" aria-label="Photo of a chrome espresso tap pouring into a teal cup"></div>

<h2 class="impact-heading script-heading abs">Be a Part of the Impact</h2>
<div class="impact-rule rule abs"><span class="p"></span><span class="g"></span><span class="b"></span></div>

<div class="cert abs" style="left:85px"><div class="disc"><div class="face" style="background:var(--pink)">
  <svg viewBox="0 0 48 48"><circle cx="24" cy="24" r="17"/><path d="M16 24.5l5.5 5.5L32.5 19"/></svg>
</div></div><div class="name">True Ledger</div></div>

<div class="cert abs" style="left:256px"><div class="disc"><div class="face" style="background:var(--green)">
  <svg viewBox="0 0 48 48"><path d="M11 37C11 20 22 11 38 10c0 17-9 27-25 27z"/><path d="M11 37L30 18"/></svg>
</div></div><div class="name">Organic</div></div>

<div class="cert abs" style="left:427px"><div class="disc"><div class="face" style="background:var(--blue)">
  <svg viewBox="0 0 48 48"><path d="M24 8l10 14h-5l8 11H11l8-11h-5z"/><path d="M24 33v8"/></svg>
</div></div><div class="name">Leaf Harbour</div></div>

<div class="cert abs" style="left:597px"><div class="disc"><div class="face" style="background:var(--pink)">
  <svg viewBox="0 0 48 48"><path d="M24 39S9 30 9 19a7.5 7.5 0 0 1 15-2 7.5 7.5 0 0 1 15 2c0 11-15 20-15 20z"/></svg>
</div></div><div class="name">Café Solvera</div></div>

<div class="cert abs" style="left:767px"><div class="disc"><div class="face" style="background:var(--green)">
  <svg viewBox="0 0 48 48"><path d="M24 32s-9-8-9-15a9 9 0 0 1 18 0c0 7-9 15-9 15z"/><circle cx="24" cy="17" r="3"/><ellipse cx="24" cy="36" rx="13" ry="4"/></svg>
</div></div><div class="name">Lune Verte</div></div>

<div class="cert abs" style="left:937px"><div class="disc"><div class="face" style="background:var(--blue)">
  <svg viewBox="0 0 48 48"><circle cx="24" cy="24" r="17"/><path d="M24 36V14"/><path d="M24 20c-3-1-5-3-5-6 3 0 5 2 5 6zM24 20c3-1 5-3 5-6-3 0-5 2-5 6zM24 27c-3-1-5-3-5-6 3 0 5 2 5 6zM24 27c3-1 5-3 5-6-3 0-5 2-5 6z"/><path d="M12 12l24 24"/></svg>
</div></div><div class="name">gluten free</div></div>

<footer class="site-footer abs"></footer>
<div class="footer-brand abs">Café Lune Verte</div>
<div class="footer-col abs" style="left:498px">
  <svg width="14" height="18" viewBox="0 0 14 18"><path d="M7 0C3.1 0 0 3.1 0 7c0 5 7 11 7 11s7-6 7-11c0-3.9-3.1-7-7-7zm0 9.5A2.5 2.5 0 1 1 7 4.5a2.5 2.5 0 0 1 0 5z" fill="#fff"/></svg>
  5688 Rue de Castelmoor<br>Castelmoor, QC K2M 4R8
</div>
<div class="footer-col abs" style="left:752px">
  <svg width="17" height="17" viewBox="0 0 24 24"><path d="M6.6 10.8a15.1 15.1 0 0 0 6.6 6.6l2.2-2.2a1 1 0 0 1 1-.25 11.4 11.4 0 0 0 3.6.57 1 1 0 0 1 1 1V20a1 1 0 0 1-1 1A17 17 0 0 1 3 4a1 1 0 0 1 1-1h3.5a1 1 0 0 1 1 1c0 1.25.2 2.45.57 3.57a1 1 0 0 1-.25 1z" fill="#fff"/></svg>
  Call:<br>(555) 014-2290
</div>
<div class="footer-col abs" style="left:934px">
  <svg width="17" height="17" viewBox="0 0 24 24"><path d="M2 5h20v14H2z" fill="#fff"/><path d="M2 5l10 8 10-8" fill="none" stroke="#2b2b2b" stroke-width="2"/></svg>
  Email:<br>info.luneverte.example
</div>
<div class="footer-rule abs"></div>
<div class="copyright abs">2022 Café Lune Verte. All Rights Reserved.</div>

</body>
</html>
```